Wrenhollow Acres Organic Flower Farm, Farmer Florist

I am a flower grower and florist, so I do everything from the field to the vase. I want to include my website, phone, email and instagram

```html
<!DOCTYPE html>
<html lang="en">
<head>
<meta charset="utf-8">
<title>Wrenhollow Acres – Business Card</title>
<link rel="stylesheet" href="https://fonts.googleapis.com/css2?family=Cinzel:wght@400&family=Montserrat:wght@400&display=swap">
<style>
  :root {
    --maroon: #431a20;
    --maroon-light: #5a2c31;
    --blush: #f08e8e;
    --blush-icon: #f39d9c;
    --white: #ffffff;
  }
  * { margin: 0; padding: 0; box-sizing: border-box; }
  html, body {
    width: 1200px;
    height: 686px;
    overflow: hidden;
    background: var(--white);
  }
  .card {
    position: relative;
    width: 1200px;
    height: 686px;
    overflow: hidden;
    background: var(--white);
  }
  .card__backdrop {
    position: absolute;
    inset: 0;
    width: 1200px;
    height: 686px;
  }
  .card__botanical {
    position: absolute;
    right: 0;
    top: 0;
    width: 200px;
    height: 686px;
    background: linear-gradient(180deg, rgba(120,70,72,0.35) 0%, rgba(110,62,66,0.25) 55%, rgba(90,44,49,0.1) 100%);
    border-radius: 100px 0 0 100px;
  }
  .brand {
    position: absolute;
    left: 0;
    top: 0;
    width: 624px;
    height: 686px;
    display: flex;
    align-items: center;
    justify-content: center;
  }
  .brand__name {
    font-family: "Cinzel", "Times New Roman", serif;
    font-weight: 400;
    font-size: 64px;
    letter-spacing: 2px;
    color: var(--maroon);
    text-transform: uppercase;
    white-space: nowrap;
  }
  .contacts {
    position: absolute;
    left: 764px;
    top: 194px;
    list-style: none;
  }
  .contacts__item {
    display: flex;
    align-items: center;
    height: 60px;
    margin-bottom: 31px;
  }
  .contacts__icon {
    flex: none;
    width: 60px;
    height: 60px;
    border-radius: 50%;
    background: var(--blush-icon);
    display: flex;
    align-items: center;
    justify-content: center;
  }
  .contacts__icon svg { width: 28px; height: 28px; }
  .contacts__text {
    margin-left: 19px;
    font-family: "Montserrat", Arial, sans-serif;
    font-size: 21px;
    color: var(--white);
    white-space: nowrap;
  }
</style>
</head>
<body>
<main class="card">
  <svg class="card__backdrop" viewBox="0 0 1050 600" aria-hidden="true">
    <circle cx="1000" cy="425" r="472" fill="var(--blush)"/>
    <circle cx="1005" cy="428" r="465" fill="var(--white)"/>
    <circle cx="995" cy="430" r="447" fill="var(--maroon)"/>
  </svg>

  <div class="card__botanical" role="img" aria-label="Faint botanical flower silhouette decoration"></div>

  <section class="brand">
    <h1 class="brand__name">Wrenhollow</h1>
  </section>

  <ul class="contacts">
    <li class="contacts__item">
      <span class="contacts__icon">
        <svg viewBox="0 0 24 24" fill="var(--white)" aria-hidden="true">
          <path d="M6.6 10.8a15.1 15.1 0 0 0 6.6 6.6l2.2-2.2a1 1 0 0 1 1-.25 11.4 11.4 0 0 0 3.6.57 1 1 0 0 1 1 1V20a1 1 0 0 1-1 1A17 17 0 0 1 3 4a1 1 0 0 1 1-1h3.5a1 1 0 0 1 1 1c0 1.25.2 2.45.57 3.57a1 1 0 0 1-.25 1z"/>
        </svg>
      </span>
      <span class="contacts__text">(708) 5550 1426</span>
    </li>
    <li class="contacts__item">
      <span class="contacts__icon">
        <svg viewBox="0 0 24 24" aria-hidden="true">
          <rect x="2" y="5" width="20" height="14" rx="1" fill="var(--white)"/>
          <path d="M2.5 5.5 12 13l9.5-7.5" fill="none" stroke="var(--blush-icon)" stroke-width="1.6"/>
        </svg>
      </span>
      <span class="contacts__text">hello@wrenhollowacres.com.au</span>
    </li>
    <li class="contacts__item">
      <span class="contacts__icon">
        <svg viewBox="0 0 24 24" fill="none" stroke="var(--white)" stroke-width="1.8" aria-hidden="true">
          <circle cx="12" cy="12" r="9.5"/>
          <ellipse cx="12" cy="12" rx="4" ry="9.5"/>
          <path d="M2.5 12h19M4 7h16M4 17h16"/>
        </svg>
      </span>
      <span class="contacts__text">www.wrenhollowacres.com</span>
    </li>
    <li class="contacts__item">
      <span class="contacts__icon"></span>
      <span class="contacts__text">wrenhollowoninstagram</span>
    </li>
  </ul>
</main>
</body>
</html>
```